Website Design for Australian Vocational Education organisation

A website for an Educational organisation. A responsive design that works well on a laptop desktop or a mobile phone. Is easy to navigate. Be able to start small and add new pages and features at a later stage.
Requires the logo, the name of company, home page with hero shots, enquiry form that forwards to a specified email address
links to social media, home page. We need a home page, and two more templates for sub pages.
Must not be a typical common design.

current website www.qvtl.edu.au
this needs to look different. logo should remain the same.

Target Market(s)

across age groups from 18-70. so must be inutitive. some will be tech savvy and others not.

Industry/Entity Type

Education

Coding

Coded - Design and coding required

Colors

Designer to choose colors to be used in the design.

Requirements
Must have
• responsive design, video, photo gallery, hero image, social media links, news feed, calendar, shopping cart, enquiry form
Nice to have
• Sample website
• www.bluegumlearning.com.au
• but should not be similar to this. it must look different. the sample is to give an idea on the various pages and links that will be required

```html
<!DOCTYPE html>
<html lang="en">
<head>
<meta charset="utf-8">
<title>Southern Institute of Applied Skills</title>
<link href="https://fonts.googleapis.com/css2?family=Poppins:wght@300;400;500;600;700&display=swap" rel="stylesheet">
<style>
:root{
  --navy:#232a5c;
  --red:#e3202a;
  --ink:#1d1d1d;
  --grey:#666;
  --light:#f5f5f5;
  --panel:#f3f3f3;
  --footer:#1b1f2b;
  --footer-box:#262c3a;
  --green:#36b52c;
  --purple:#9b3fbf;
  --orange:#f39c12;
  --blue:#2e8ee6;
}
*{margin:0;padding:0;box-sizing:border-box}
html,body{width:1200px;height:2706px;overflow:hidden}
body{font-family:'Poppins',sans-serif;color:var(--ink);background:#fff;position:relative}
section,header,footer,div{position:relative}
.abs{position:absolute}

/* top bar */
.topbar{height:35px;background:var(--navy);color:#fff;font-size:10px}
.topbar .org{left:235px;top:11px}
.topbar .links{left:704px;top:11px;display:flex;gap:10px;align-items:center}
.topbar .links .sep{width:1px;height:16px;background:#6a70a0}
.social{display:flex;gap:8px}
.social span{width:14px;height:14px;border-radius:50%;background:#fff;display:block}
.topbar .social{left:906px;top:10px}

/* header */
.site-header{height:65px;background:#fff;border-bottom:1px solid #eee}
.brand{left:235px;top:8px;display:flex;gap:6px;align-items:center}
.brand .mark{width:44px;height:44px;background:var(--red)}
.brand .name{font-size:10px;font-weight:600;color:var(--navy);line-height:12px;width:68px}
.nav{left:385px;top:28px;display:flex;gap:26px;font-size:9px;font-weight:500;letter-spacing:.3px}
.call{left:731px;top:20px;display:flex;gap:8px;align-items:center}
.call .ring{width:22px;height:22px;border:1px solid var(--red);border-radius:50%;display:flex;align-items:center;justify-content:center}
.call .txt{font-size:9px;line-height:12px;color:#333}
.call .txt b{font-weight:500}
.or{left:838px;top:28px;font-size:9px;font-style:italic;color:#555}
.btn-enquiry{left:865px;top:20px;width:101px;height:26px;background:var(--red);color:#fff;border-radius:13px;font-size:9px;font-weight:500;display:flex;align-items:center;justify-content:center}

/* hero */
.hero{height:397px;background:linear-gradient(90deg,#6f8391 0%,#7a8b95 45%,#8a7a5a 65%,#6b5335 85%,#3a2e22 100%)}
.hero h1{left:233px;top:122px;font-size:33px;font-weight:600;color:#fff}
.search{left:235px;top:189px;width:302px;height:46px;background:#fff;border-radius:23px}
.search span{left:24px;top:16px;font-size:11px;font-style:italic;color:#888}
.search .go{right:-3px;top:4px;width:38px;height:38px;border-radius:50%;background:var(--red);display:flex;align-items:center;justify-content:center}

/* courses */
.intro{height:496px}
.section-title{font-size:19px;font-weight:600;letter-spacing:.3px}
.section-title::after{content:"";display:block;width:38px;height:3px;background:var(--red);margin-top:12px}
.courses-title{left:235px;top:47px}
.course{left:235px;width:481px;height:159px;background:var(--light)}
.course.business{top:112px;border-right:2px solid var(--green)}
.course.hospitality{top:295px;border-right:2px solid var(--purple)}
.course .icon{left:35px;top:60px}
.course h3{left:106px;top:26px;font-size:15px;font-weight:500}
.course p{left:106px;top:52px;width:576px;font-size:8.8px;line-height:16.2px;color:#333;text-align:justify;width:347px}
.enquiry{left:735px;top:0;width:232px;height:496px;background:var(--panel)}
.enquiry .section-title{left:16px;top:47px}
.field{left:16px;width:200px;height:30px;background:#fff;border:1px solid #e2e2e2;font-size:9px;color:#555;padding:9px 10px}
.field.select::after{content:"";position:absolute;right:12px;top:13px;border:3px solid transparent;border-top:4px solid #aaa}
.submit{left:16px;top:409px;width:200px;height:31px;background:var(--red);color:#fff;font-size:11px;font-weight:600;display:flex;align-items:center;justify-content:center}

/* gallery */
.gallery{height:701px;background:var(--light)}
.gallery .section-title{left:0;width:1200px;top:45px;text-align:center}
.gallery .section-title::after{margin:12px auto 0}
.grid{left:0;top:129px;width:1200px;display:grid;grid-template-columns:repeat(4,300px);grid-template-rows:240px 241px}
.tile{display:block}
.t1{background:linear-gradient(135deg,#3b3a38,#6e6860)}
.t2{background:linear-gradient(135deg,#d9dadc,#a9a8a6)}
.t3{background:linear-gradient(135deg,#e03a32,#c41f1c);display:flex;flex-direction:column;align-items:center;justify-content:center;color:#fff}
.t4{background:linear-gradient(135deg,#cfd3d6,#5a4a4a)}
.t5{background:linear-gradient(135deg,#3b3b3b,#4c6a91)}
.t6{background:linear-gradient(135deg,#5a3a24,#a06a3c)}
.t7{background:linear-gradient(135deg,#5f6b70,#8a6a3c)}
.t8{background:linear-gradient(135deg,#e4e2df,#8d8a86)}
.t3 .acts{display:flex;gap:12px;margin-bottom:12px}
.t3 .acts span{width:30px;height:30px;border-radius:50%;background:#fff;display:flex;align-items:center;justify-content:center}
.t3 b{font-size:14px;font-weight:600;letter-spacing:.5px}
.t3 small{font-size:10px;margin-top:4px}
.load{left:544px;top:642px;width:112px;height:26px;border:1px solid var(--red);color:var(--red);font-size:10px;font-weight:500;display:flex;align-items:center;justify-content:center;background:#fff}

/* stats */
.stats{height:152px;background:linear-gradient(90deg,#2e3238,#3b3f45 50%,#2e3238);color:#fff}
.stat{top:22px;width:240px;text-align:center}
.stat .num{font-size:19px;font-weight:600;margin-top:6px}
.stat p{font-size:9px;line-height:16px;margin-top:6px}
.stat .ico{height:38px;display:flex;justify-content:center}

/* news */
.news{height:419px}
.news .section-title{font-size:15px}
.news-title{left:235px;top:48px}
.video-title{left:735px;top:48px}
.arrows{left:672px;top:48px;display:flex;gap:2px}
.arrows span{width:20px;height:20px;border:1px solid var(--red);display:flex;align-items:center;justify-content:center}
.card{top:107px;width:232px;height:250px;background:#f7f7f7}
.card .photo{height:150px}
.card .date{left:19px;top:168px;width:39px;height:55px;border:1px dashed var(--red);text-align:center;font-size:9px}
.card .date b{display:block;color:var(--red);font-size:14px;font-weight:500;margin-top:7px}
.card h4{left:70px;top:166px;font-size:11px;font-weight:500;line-height:16px;width:150px}
.card p{left:70px;top:206px;font-size:8.5px;line-height:15px;color:#444;width:150px}
.video{left:735px;top:107px;width:232px;height:250px;background:linear-gradient(135deg,#2d3a3a,#3e4c4c 60%,#b0a79a)}
.video .play{left:94px;top:104px;width:44px;height:44px;border-radius:50%;background:var(--red);display:flex;align-items:center;justify-content:center}

/* footer */
.footer{height:441px;background:linear-gradient(#fff 0,#fff 65px,var(--footer) 65px)}
.newsletter{left:235px;top:0;width:732px;height:128px;background:var(--footer-box);text-align:center;color:#fff}
.newsletter h2{font-size:16px;font-weight:600;padding-top:20px}
.newsletter p{font-size:10px;color:#ccc;margin-top:3px}
.newsletter .mail{left:169px;top:88px;width:395px;height:20px;border-bottom:1px solid #4a5166;text-align:left;font-size:8px;color:#777}
.newsletter .mail svg{position:absolute;right:2px;top:0}
.f-brand{left:235px;top:174px;display:flex;gap:6px;align-items:center}
.f-brand .mark{width:44px;height:44px;background:#fff}
.f-brand .name{font-size:10px;font-weight:600;color:#fff;line-height:12px;width:70px}
.contact{left:235px;top:245px;font-size:8.5px;color:#aab}
.contact li{list-style:none;display:flex;gap:10px;margin-bottom:12px;line-height:13px}
.f-col h5{font-size:11px;font-weight:500;color:#fff}
.f-col ul{list-style:none;margin-top:24px;font-size:8.5px;color:#aab}
.f-col li{margin-bottom:12px}
.f-col li::before{content:"› ";color:#aab}
.quick{left:416px;top:174px}
.coursecol{left:511px;top:174px}
.calendar{left:735px;top:164px;width:232px;height:200px;background:var(--footer-box);color:#fff}
.calendar .head{display:flex;justify-content:space-between;align-items:center;padding:16px 20px 6px;font-size:12px;font-weight:600}
.calendar table{width:208px;margin:0 12px;border-collapse:collapse;font-size:9.5px;text-align:center}
.calendar th{font-weight:400;height:20px}
.calendar td{height:25px}
.calendar td.today span{display:inline-block;width:20px;height:20px;line-height:20px;border-radius:50%;background:var(--red)}
.calendar td.bold{font-weight:600}
.copyright{height:48px;background:var(--footer);border-top:1px solid #2c3243}
.copyright p{left:235px;top:17px;font-size:10px;color:#6b7080}
.copyright .social{left:886px;top:14px;gap:12px}
.copyright .social span{width:20px;height:20px;background:#2c3243}
</style>
</head>
<body>

<div class="topbar">
  <span class="abs org">Southern Institute of Applied Skills (SIAS)</span>
  <div class="abs links">
    <svg width="14" height="12" viewBox="0 0 14 12"><path d="M1 1h2l2 7h7l1-5H4" fill="none" stroke="#e3202a" stroke-width="1.3"/><circle cx="6" cy="10.5" r="1" fill="#e3202a"/><circle cx="11" cy="10.5" r="1" fill="#e3202a"/></svg>
    <span>Shopping Cart</span><span class="sep"></span><span>Sign In / Register</span>
  </div>
  <div class="abs social"><span></span><span></span><span></span></div>
</div>

<header class="site-header">
  <div class="abs brand"><div class="mark"></div><div class="name">SOUTHERN INSTITUTE OF APPLIED SKILLS</div></div>
  <nav class="abs nav"><span>HOME</span><span>ABOUT US</span><span>COURSES ⌄</span><span>STUDENTS</span><span>CONTACT US</span></nav>
  <div class="abs call">
    <div class="ring"><svg width="11" height="11" viewBox="0 0 12 12"><path d="M3 1l2 3-1.2 1.2a7 7 0 003 3L8 7l3 2-1 2C5 11 1 7 1 2z" fill="none" stroke="#e3202a" stroke-width="1"/></svg></div>
    <div class="txt"><b>Call Us:</b><br>+61 400 555 218</div>
  </div>
  <span class="abs or">(or)</span>
  <div class="abs btn-enquiry">ENQUIRY NOW</div>
</header>

<section class="hero" role="img" aria-label="Hero photo of two colleagues discussing work at a laptop in an office">
  <h1 class="abs">How can we help you?</h1>
  <div class="abs search"><span class="abs">Search here...</span>
    <div class="abs go"><svg width="14" height="14" viewBox="0 0 14 14"><circle cx="6" cy="6" r="4.3" fill="none" stroke="#fff" stroke-width="1.6"/><path d="M9.2 9.2L13 13" stroke="#fff" stroke-width="1.6"/></svg></div>
  </div>
</section>

<section class="intro">
  <h2 class="abs section-title courses-title">TAKE A PEEK AT OUR COURSES</h2>
  <article class="abs course business">
    <svg class="abs icon" width="42" height="38" viewBox="0 0 42 38"><rect x="2" y="8" width="38" height="28" rx="3" fill="none" stroke="#36b52c" stroke-width="2"/><path d="M15 8V3h12v5M2 18h38M19 18v4h4v-4" fill="none" stroke="#36b52c" stroke-width="2"/></svg>
    <h3 class="abs">BUSINESS</h3>
    <p class="abs">Business training program involve various aspects of managing scarce resources in a business entity and supporting a business by production/planning, decision making, project management as well as allocating human resources and finances while, at the same time, carrying out organisational goals, policies and procedures.</p>
  </article>
  <article class="abs course hospitality">
    <svg class="abs icon" width="42" height="42" viewBox="0 0 42 42"><path d="M11 24a8 8 0 01-2-15 9 9 0 0112-5 9 9 0 0112 5 8 8 0 01-2 15v14H11z" fill="none" stroke="#9b3fbf" stroke-width="2"/><path d="M11 31h20M17 24v5M25 24v5" stroke="#9b3fbf" stroke-width="2"/></svg>
    <h3 class="abs">HOSPITALITY</h3>
    <p class="abs">The hotel and catering industry is a major component of the Australian tourism industry. The ongoing boom in travel spells equally golden times for the hotel and catering industry, helping it become the fastest growing industry in the world. Hospitality provides a fast paced and rewarding career and it is growing quickly. If you are the kind of person who enjoys people and has a "can do"</p>
  </article>
  <aside class="abs enquiry">
    <h2 class="abs section-title">ENQUIRY FORM</h2>
    <div class="abs field" style="top:103px">Name*</div>
    <div class="abs field" style="top:141px">Email*</div>
    <div class="abs field" style="top:180px">Phone*</div>
    <div class="abs field" style="top:218px">Postcode*</div>
    <div class="abs field select" style="top:256px">Interested in?*</div>
    <div class="abs field select" style="top:294px">Qualification?*</div>
    <div class="abs field select" style="top:332px">Are you currently</div>
    <div class="abs field select" style="top:370px">Time for call</div>
    <div class="abs submit">SUBMIT</div>
  </aside>
</section>

<section class="gallery">
  <h2 class="abs section-title">OUR GALLERY</h2>
  <div class="abs grid">
    <div class="tile t1" role="img" aria-label="Business people shaking hands in an office"></div>
    <div class="tile t2" role="img" aria-label="Team meeting around a white table"></div>
    <div class="tile t3" role="img" aria-label="Hospitality student serving food, with overlay">
      <div class="acts">
        <span><svg width="14" height="10" viewBox="0 0 14 10"><path d="M1 5s2.5-4 6-4 6 4 6 4-2.5 4-6 4-6-4-6-4z" fill="#e3202a"/><circle cx="7" cy="5" r="1.8" fill="#fff"/></svg></span>
        <span><svg width="12" height="12" viewBox="0 0 12 12"><path d="M5 7l2-2M4 5L2.5 6.5a2 2 0 003 3L7 8M8 7l1.5-1.5a2 2 0 00-3-3L5 4" fill="none" stroke="#e3202a" stroke-width="1.3"/></svg></span>
      </div>
      <b>HOSPITALITY</b><small>Courses</small>
    </div>
    <div class="tile t4" role="img" aria-label="Barista preparing drinks at a counter"></div>
    <div class="tile t5" role="img" aria-label="Students working on laptops in a library"></div>
    <div class="tile t6" role="img" aria-label="Restaurant interior with pendant lamps"></div>
    <div class="tile t7" role="img" aria-label="Colleagues discussing work at a laptop"></div>
    <div class="tile t8" role="img" aria-label="Group of students studying together at a table"></div>
  </div>
  <div class="abs load">LOAD MORE</div>
</section>

<section class="stats" role="region" aria-label="Statistics">
  <div class="abs stat" style="left:249px">
    <div class="ico"><svg width="40" height="36" viewBox="0 0 40 36"><path d="M2 12l8-8 8 4 6-3 6 3 8 4-8 12-4 4-4-4-4 4-4-4-6-4z" fill="none" stroke="#fff" stroke-width="2"/><path d="M16 14l6-4 8 8" fill="none" stroke="#fff" stroke-width="2"/></svg></div>
    <div class="num" style="color:var(--green)">2170000</div>
    <p>ACTIVELY TRADING BUSINESS<br>IN AUSTRALIA</p>
  </div>
  <div class="abs stat" style="left:499px">
    <div class="ico"><svg width="42" height="34" viewBox="0 0 42 34"><path d="M21 6C15 2 8 2 3 4v26c5-2 12-2 18 2 6-4 13-4 18-2V4c-5-2-12-2-18 2z" fill="#fff"/><path d="M21 6v26" stroke="#3b3f45" stroke-width="2"/></svg></div>
    <div class="num" style="color:var(--orange)">984000</div>
    <p>PERSONAL EMPLOYED BY EDUCATION AND<br>TRAINING INDUSTRY</p>
  </div>
  <div class="abs stat" style="left:730px">
    <div class="ico"><svg width="24" height="40" viewBox="0 0 24 40"><rect x="1" y="2" width="22" height="6" rx="2" fill="#fff"/><path d="M3 10h18l-3 28H6z" fill="#fff"/><path d="M7 18l10 10" stroke="#3b3f45" stroke-width="2"/></svg></div>
    <div class="num" style="color:var(--blue)">9</div>
    <p>CUPS OF COFFEE PER<br>ADULT WEEK</p>
  </div>
</section>

<section class="news">
  <h2 class="abs section-title news-title">LATEST NEWS</h2>
  <div class="abs arrows">
    <span><svg width="6" height="8" viewBox="0 0 6 8"><path d="M5 1L2 4l3 3" fill="none" stroke="#e3202a" stroke-width="1.2"/></svg></span>
    <span><svg width="6" height="8" viewBox="0 0 6 8"><path d="M1 1l3 3-3 3" fill="none" stroke="#e3202a" stroke-width="1.2"/></svg></span>
  </div>
  <h2 class="abs section-title video-title">VIDEO TOUR</h2>
  <article class="abs card" style="left:235px">
    <div class="photo" role="img" aria-label="Office meeting around a table" style="background:linear-gradient(135deg,#d9dadc,#a9a8a6)"></div>
    <div class="abs date"><b>21</b>AUG</div>
    <h4 class="abs">Lorem ipsum dolor sit amet, consectetur</h4>
    <p class="abs">Curabitur a augue lorem.<br>Vivamus laoreet augue urna...</p>
  </article>
  <article class="abs card" style="left:485px">
    <div class="photo" role="img" aria-label="Students studying on laptops" style="background:linear-gradient(135deg,#3b3b3b,#4c6a91)"></div>
    <div class="abs date"><b>21</b>AUG</div>
    <h4 class="abs">Lorem ipsum dolor sit amet, consectetur</h4>
    <p class="abs">Curabitur a augue lorem.<br>Vivamus laoreet augue urna...</p>
  </article>
  <div class="abs video" role="img" aria-label="Video tour thumbnail of a presenter beside a planning board">
    <div class="abs play"><svg width="16" height="18" viewBox="0 0 16 18"><path d="M2 1l13 8-13 8z" fill="#fff"/></svg></div>
  </div>
</section>

<footer class="footer">
  <div class="abs newsletter">
    <h2>Subscribe our Newsletter</h2>
    <p>Leave your details if you'd like to receive updates and news from us</p>
    <div class="abs mail">Enter your email here
      <svg width="14" height="12" viewBox="0 0 14 12"><path d="M1 6l12-5-3 10-3-3-2 3V7z" fill="#e3202a"/></svg>
    </div>
  </div>
  <div class="abs f-brand"><div class="mark"></div><div class="name">SOUTHERN INSTITUTE OF APPLIED SKILLS</div></div>
  <ul class="abs contact">
    <li><svg width="10" height="12" viewBox="0 0 10 12"><path d="M5 11S1 7 1 4.5a4 4 0 018 0C9 7 5 11 5 11z" fill="none" stroke="#aab"/><circle cx="5" cy="4.5" r="1.3" fill="#aab"/></svg><span>12 Wattle Street, Bruce<br>ACT 2617</span></li>
    <li><svg width="11" height="11" viewBox="0 0 12 12"><path d="M3 1l2 3-1.2 1.2a7 7 0 003 3L8 7l3 2-1 2C5 11 1 7 1 2z" fill="none" stroke="#aab"/></svg><span>+61 400 555 218</span></li>
    <li><svg width="12" height="10" viewBox="0 0 12 10"><rect x="1" y="1" width="10" height="8" fill="none" stroke="#aab"/><path d="M1 1l5 4 5-4" fill="none" stroke="#aab"/></svg><span>info@sias.edu.au</span></li>
    <li><svg width="11" height="11" viewBox="0 0 12 12"><circle cx="6" cy="6" r="5" fill="none" stroke="#aab"/><path d="M6 3v3l2 1" fill="none" stroke="#aab"/></svg><span>Mon - Fri 8.30 AM - 04.30 PM</span></li>
  </ul>
  <div class="abs f-col quick"><h5>QUICK LINK</h5>
    <ul><li>Home</li><li>About Us</li><li>Courses</li><li>Students</li><li>Contact Us</li></ul>
  </div>
  <div class="abs f-col coursecol"><h5>COURSES</h5>
    <ul><li>Diploma of Hospitality Management</li><li>Diploma of Leadership and Management</li><li>Certificate IV in Commercial Cookery</li></ul>
  </div>
  <div class="abs calendar">
    <div class="head">
      <svg width="7" height="10" viewBox="0 0 7 10"><path d="M6 1L2 5l4 4" fill="none" stroke="#fff" stroke-width="1.5"/></svg>
      <span>AUGUST 2019</span>
      <svg width="7" height="10" viewBox="0 0 7 10"><path d="M1 1l4 4-4 4" fill="none" stroke="#fff" stroke-width="1.5"/></svg>
    </div>
    <table>
      <tr><th>Sun</th><th>Mon</th><th>Tue</th><th>Wed</th><th>Thu</th><th>Fri</th><th>Sat</th></tr>
      <tr><td></td><td></td><td></td><td></td><td>1</td><td>2</td><td>3</td></tr>
      <tr><td>4</td><td>5</td><td>6</td><td>7</td><td>8</td><td>9</td><td>10</td></tr>
      <tr><td>11</td><td>12</td><td>13</td><td>14</td><td>15</td><td>16</td><td>17</td></tr>
      <tr><td>18</td><td>19</td><td>20</td><td class="bold">21</td><td class="today"><span>22</span></td><td>23</td><td>24</td></tr>
      <tr><td>25</td><td>26</td><td>27</td><td>28</td><td>29</td><td>30</td><td>31</td></tr>
    </table>
  </div>
</footer>

<div class="copyright">
  <p class="abs">Copyright © 2019, Southern Institute of Applied Skills Pty Ltd | ACN: 612004781 | RTO: 40912</p>
  <div class="abs social"><span></span><span></span><span></span></div>
</div>

</body>
</html>
```